Crestline Alloy Partners Business Card

Design a business card for a new company. Crestline Alloy Partners is a subsidiary of KVT, Inc. (www.kvtreclaims.example)

Target Market(s)

B2B, Manufactures

Industry/Entity Type

Recycling

Contact Information for Business Card

Crestline Alloy Partners, LLC.
40517 West Fennimore Lane
Dorwick IL 60594
P: (555) 309-4462
F: (555) 309-4461
www.crestap.example
Email@crestap.example

Font styles to use
Sans Serif

Requirements
Must have
• A KVT, Inc. subsidiary company.
Nice to have
• Recycling Solutions. Uncompromised. (slogan)

```html
<!DOCTYPE html>
<html lang="en">
<head>
<meta charset="utf-8">
<title>Crestline Alloy Partners Business Card</title>
<link href="https://fonts.googleapis.com/css2?family=Open+Sans:wght@400;600;700&display=swap" rel="stylesheet">
<style>
  :root {
    --bg: #ece8e2;
    --green-deep: #0d3f1c;
    --green-mid: #1f6a35;
    --green-light: #3f8a55;
    --lime: #b7d433;
    --white: #ffffff;
    --ink-green: #245c32;
    --divider: rgba(255,255,255,0.35);
  }
  * { margin: 0; padding: 0; box-sizing: border-box; }
  html, body { width: 1200px; height: 913px; overflow: hidden; }
  body {
    background: var(--bg);
    font-family: "Open Sans", Arial, sans-serif;
    position: relative;
  }
  .card {
    position: absolute;
    width: 520px;
    height: 300px;
    border-radius: 18px;
    box-shadow: 0 10px 26px rgba(0,0,0,0.22);
    overflow: hidden;
  }
  .card-front {
    left: 70px; top: 140px;
    background: linear-gradient(160deg, var(--green-light) 0%, var(--green-mid) 40%, var(--green-deep) 100%);
    color: var(--white);
  }
  .card-back {
    left: 610px; top: 470px;
    background: var(--white);
  }
  .parent-line {
    position: absolute;
    left: 40px; top: 38px;
    font-size: 17px;
    font-weight: 600;
    letter-spacing: 0.3px;
  }
  .parent-line .accent { color: var(--lime); }
  .brand-front {
    position: absolute;
    left: 40px; top: 110px;
    width: 230px;
    display: flex;
    align-items: center;
    gap: 12px;
  }
  .brand-mark {
    flex: none;
    width: 22px; height: 22px;
    border-radius: 50%;
    background: var(--white);
  }
  .brand-name {
    font-size: 27px;
    font-weight: 700;
    line-height: 1.15;
  }
  .divider {
    position: absolute;
    left: 300px; top: 95px;
    width: 1px; height: 170px;
    background: var(--divider);
  }
  .contact {
    position: absolute;
    left: 320px; top: 90px;
    font-size: 13px;
    line-height: 1.45;
  }
  .contact .name { font-size: 18px; font-weight: 700; line-height: 1.2; letter-spacing: 0.3px; }
  .contact .role { color: var(--lime); font-size: 13px; font-weight: 600; margin-bottom: 6px; }
  .contact .address { margin-bottom: 4px; }
  .contact-row { display: flex; align-items: center; gap: 8px; }
  .contact-row svg { width: 12px; height: 12px; flex: none; }
  .brand-back {
    position: absolute;
    left: 0; right: 0; top: 95px;
    display: flex;
    justify-content: center;
    align-items: center;
    gap: 14px;
    color: var(--ink-green);
  }
  .brand-back .brand-mark { background: var(--ink-green); }
  .brand-back .brand-name { font-size: 30px; }
  .slogan {
    position: absolute;
    left: 0; right: 0; bottom: 70px;
    text-align: center;
    color: var(--ink-green);
    font-size: 15px;
    font-weight: 600;
    letter-spacing: 1.4px;
  }
</style>
</head>
<body>
  <section class="card card-front">
    <p class="parent-line">A KVT, LNC. <span class="accent">SUBSIDIARY COMPANY</span></p>
    <div class="brand-front">
      <span class="brand-mark"></span>
      <span class="brand-name">Crestline Alloy Partners</span>
    </div>
    <div class="divider"></div>
    <div class="contact">
      <p class="name">DALE MORROW</p>
      <p class="role">OWNER</p>
      <p class="address">40517 West Fennimore Lane<br>Dorwick IL 60594</p>
      <p class="contact-row">
        <svg viewBox="0 0 12 12"><path d="M2.5 1l2 2.2-1 1.3a7 7 0 0 0 4 4l1.3-1 2.2 2-1.2 1.5C5 11 1 7 1 2.3z" fill="var(--lime)"/></svg>
        (555) 309-4462
      </p>
      <p class="contact-row">
        <svg viewBox="0 0 12 12"><rect x="2" y="1" width="8" height="4" fill="var(--lime)"/><rect x="1" y="5" width="10" height="5" rx="1" fill="var(--lime)"/></svg>
        (555) 309-4461
      </p>
      <p class="contact-row">
        <svg viewBox="0 0 12 12"><circle cx="6" cy="6" r="5" fill="none" stroke="var(--lime)" stroke-width="1.2"/><path d="M1 6h10M6 1c-2.5 3-2.5 7 0 10M6 1c2.5 3 2.5 7 0 10" fill="none" stroke="var(--lime)" stroke-width="1"/></svg>
        www.crestap.example
      </p>
      <p class="contact-row">
        <svg viewBox="0 0 12 12"><rect x="1" y="2.5" width="10" height="7" fill="none" stroke="var(--lime)" stroke-width="1.2"/><path d="M1 2.5l5 4 5-4" fill="none" stroke="var(--lime)" stroke-width="1.2"/></svg>
        Email@crestap.example
      </p>
    </div>
  </section>

  <section class="card card-back">
    <div class="brand-back">
      <span class="brand-mark"></span>
      <span class="brand-name">Crestline Alloy Partners</span>
    </div>
    <p class="slogan">RECYCLING SOLUTIONS. UNCOMPROMISED</p>
  </section>
</body>
</html>
```